Letterhead for financial advisor-insurance agent firm

Our company, Harlow Pemberton Insurance & Investments, is an insurance (health, life, home, auto, etc) and investment brokerage offering a suite of options to meet client needs. We need letterhead that is professional and embodies strength, security and sophistication.

http://jobs.brieftrove.example/job.aspx?id=518264

Industry/Entity Type

Investment

```html
<!DOCTYPE html>
<html lang="en">
<head>
<meta charset="utf-8">
<title>Harlow Pemberton Insurance &amp; Investments — Letterhead</title>
<link rel="stylesheet" href="https://fonts.googleapis.com/css2?family=Cinzel:wght@400;600&display=swap">
<style>
  :root {
    --backdrop: #d9dadc;
    --paper: #ffffff;
    --navy: #1e2a4f;
    --slate: #6f7f8c;
    --ink: #1e2a4f;
  }
  * { margin: 0; padding: 0; box-sizing: border-box; }
  html, body {
    width: 1200px;
    height: 800px;
    overflow: hidden;
    background: var(--backdrop);
  }
  .letterhead {
    position: absolute;
    left: 331px;
    top: 20px;
    width: 538px;
    height: 760px;
    background: var(--paper);
    box-shadow: 0 2px 10px rgba(0, 0, 0, 0.18);
    overflow: hidden;
  }
  .letterhead__band {
    position: absolute;
    top: 0;
    left: 0;
    width: 538px;
    height: 48px;
    display: block;
  }
  .brand {
    position: absolute;
    top: 12px;
    left: 0;
    width: 100%;
    text-align: center;
    color: var(--ink);
    font-family: "Cinzel", serif;
  }
  .brand__square {
    display: block;
    width: 24px;
    height: 24px;
    margin: 0 auto 5px;
    border: 1.5px solid var(--ink);
  }
  .brand__name {
    display: block;
    font-size: 15px;
    font-weight: 400;
    letter-spacing: 1px;
    line-height: 1.1;
  }
  .brand__tagline {
    display: block;
    font-size: 6.5px;
    font-weight: 400;
    letter-spacing: 1.2px;
    margin-top: 2px;
  }
</style>
</head>
<body>
  <main class="letterhead">
    <svg class="letterhead__band" viewBox="0 0 538 48" aria-hidden="true">
      <rect x="0" y="0" width="538" height="40" fill="var(--navy)"/>
      <rect x="0" y="0" width="538" height="14" fill="var(--slate)"/>
      <path d="M150,40 C180,40 178,0 208,0 L330,0 C360,0 358,40 388,40 L388,48 L150,48 Z" fill="var(--paper)"/>
    </svg>
    <header class="brand">
      <span class="brand__square"></span>
      <span class="brand__name">Harlow Pemberton</span>
      <span class="brand__tagline">Insurance &amp; Investments</span>
    </header>
  </main>
</body>
</html>
```